Data Analytics Platform Website Design

Website design for a new data analytics platform called Metrica Core. I need a design that is simple but informative, professional but still sexy and that is aimed at the business professional instead of being "technical". I have a logo (picture uploaded) and also screenshots from the platform itself and I can also provide example websites from competitors that are similar in design and layout to what I need. I also have the messaging but I need help with photos, icons, font, layout, etc. I want to utilize some of the colors in the logo, but I want the overall color scheme to utilize darker blues (more serious feeling, less playful) with one accent color for highlighting. This design cannot be "fun", "playful", or "cheerful" and should instead be "professional", "serious", but still uncluttered and clean cut. However, simple does not mean easy because I want to see transitions that are clean and high level. I want the final design to be all of that while showing the company and our product as capable, serious, and reliable.

Example websites:
1. www.valdrenix.com
2. q7.ai
3. corvelane.com
4. https://www.pym.com/en_us/software/lorsa.html
5. https://www.belvoro.com/
6. gwendel.ai

Target Market(s)

Business Professionals - Government/large companies/data analytics focused

Industry/Entity Type

Data Science

Number of Pages Required

3 page

Font styles to use
Serif
Sans Serif

Requirements
Must have
• It must be clean and professional. Cannot be cluttered or too "busy". No playful or childish looks at all.
Nice to have
• I want to see professional designs but also professional concepts incorporated.
Should not have
• Should not have Comic Sans or the like, no playful or "techy" themes

```html
<!DOCTYPE html>
<html lang="en">
<head>
<meta charset="utf-8">
<title>Metrica Core – Data Analytics</title>
<link href="https://fonts.googleapis.com/css2?family=Orbitron:wght@600;700&family=Poppins:wght@400;500;600&display=swap" rel="stylesheet">
<style>
:root{
  --canvas:#f4f5f8;
  --navy:#0a1d5c;
  --ink:#0d1a44;
  --text:#3b4256;
  --deep:#0a1d4d;
  --footer:#0a1e3f;
  --accent:#2f6fe6;
  --violet:#a3a4f0;
  --sky:#5d8ff2;
  --grey:#f2f2f2;
  --white:#ffffff;
}
*{margin:0;padding:0;box-sizing:border-box}
html,body{width:1200px;height:3131px;overflow:hidden;background:var(--canvas);font-family:"Poppins",sans-serif;color:var(--text)}
.page{position:absolute;left:120px;top:70px;width:960px;background:var(--white);box-shadow:0 10px 40px rgba(10,29,92,.12)}
section,header,footer{position:relative;width:960px;overflow:hidden}
.abs{position:absolute}
.display{font-family:"Orbitron",sans-serif;font-weight:700;letter-spacing:.5px;text-transform:uppercase;color:var(--ink);line-height:1.05}
.eyebrow{font-size:12px;font-weight:600;text-transform:uppercase;color:var(--ink);letter-spacing:.3px}
.dash{display:block;height:2px;width:56px;background:var(--navy);margin-top:6px;position:relative}
.dash::after{content:"";position:absolute;left:62px;top:0;width:14px;height:2px;background:var(--navy)}
.copy{font-size:12.5px;line-height:17.5px;color:var(--text)}
.btn{display:inline-block;background:var(--navy);color:var(--white);font-size:9px;font-weight:500;text-transform:uppercase;border-radius:12px;padding:5px 13px;letter-spacing:.2px}
.btn-ghost{background:transparent;border:1.5px solid var(--white)}
/* nav */
.nav{height:47px;background:var(--white)}
.brand{display:flex;align-items:center;gap:7px;font-size:17px;color:#2a3350}
.brand-mark{width:15px;height:15px;background:var(--accent);border-radius:2px}
.nav-link{font-size:9.5px;font-weight:500;color:var(--ink);top:17px}
.nav-link.active::after{content:"";display:block;width:100%;height:2px;background:var(--navy);margin-top:5px}
/* hero */
.hero{height:427px}
.hero-bg{inset:0;background:radial-gradient(ellipse at 75% 40%,#3d63b8 0%,#1b3f8f 35%,#0c2766 70%,#081a4a 100%)}
.hero-title{color:var(--white);font-size:35px}
.hero-copy{color:#dfe6f7;font-size:12.5px;line-height:17.5px;width:350px}
/* platform */
.platform{height:448px}
.shot{background:linear-gradient(135deg,#1c2233 0%,#2b3246 30%,#e9ecf4 30.5%,#f6f7fb 100%);border-radius:6px;box-shadow:0 8px 22px rgba(0,0,0,.18)}
.context{height:475px}
/* services */
.services{height:411px;background:var(--deep)}
.services-photo{left:0;top:0;width:480px;height:411px;background:linear-gradient(120deg,#0b1e4b 0%,#17407f 45%,#0f2e63 70%,#0a1838 100%)}
.service{left:518px;display:flex;gap:17px;align-items:flex-start;width:410px}
.service-icon{flex:0 0 44px;height:44px;border:1.5px solid #cfd8ee;border-radius:50%;display:flex;align-items:center;justify-content:center}
.service h3{font-size:15px;font-weight:500;color:var(--white);margin-top:-2px}
.service p{font-size:9.8px;line-height:13px;color:#c9d3ea;margin-top:3px}
/* about */
.about{height:455px;background:var(--grey)}
/* blog */
.blog{height:454px}
.card-img{width:225px;height:101px;top:158px}
.card-body{top:256px;width:205px;background:var(--white);border-left:1.5px solid var(--navy);padding:12px 0 0 12px}
.card-body h4{font-size:10.5px;font-weight:500;line-height:14px;color:var(--ink)}
.card-date{display:flex;align-items:center;gap:8px;font-size:9px;color:var(--navy);margin:8px 0 6px}
.card-body p{font-size:9.2px;line-height:12.5px;color:var(--text)}
/* footer */
.site-footer{height:274px;background:var(--footer);color:#dbe3f3}
.f-head{font-size:13px;font-weight:600;color:var(--white);text-transform:uppercase;top:82px}
.f-list{list-style:none;top:115px;font-size:9.5px;font-weight:500;line-height:15.5px;text-transform:uppercase;color:var(--white)}
.f-contact{top:115px;font-size:10px;line-height:14px;color:var(--white)}
.f-contact div{display:flex;gap:9px;margin-bottom:8px}
.social{width:18px;height:18px;border-radius:50%;background:#dbe3f3}
</style>
</head>
<body>
<div class="page">

  <header class="nav">
    <div class="abs brand" style="left:62px;top:14px"><span class="brand-mark"></span>Metrica Core</div>
    <a class="abs nav-link active" style="left:413px">HOME</a>
    <a class="abs nav-link" style="left:479px">WHO WE ARE</a>
    <a class="abs nav-link" style="left:577px">SERVICE</a>
    <a class="abs nav-link" style="left:652px">BLOG</a>
    <a class="abs nav-link" style="left:714px">PLATFORM</a>
    <span class="abs btn" style="left:830px;top:13px;padding:4px 14px">CONTACT</span>
  </header>

  <section class="hero">
    <div class="abs hero-bg" role="img" aria-label="Hand reaching toward a glowing network globe over a blurred blue city skyline"></div>
    <h1 class="abs display hero-title" style="left:51px;top:134px">Data<br>Analytics</h1>
    <p class="abs hero-copy" style="left:51px;top:218px">Lorem ipsum dolor sit amet, consetetur sadipscing elitr, sed diam nonumy eirmod tempor invidunt ut labore et dolore magna aliquyam erat,</p>
    <span class="abs btn btn-ghost" style="left:51px;top:286px">Get Started</span>
  </section>

  <section class="platform">
    <div class="abs" style="left:85px;top:117px">
      <div class="eyebrow">Our Platform</div>
      <h2 class="display" style="font-size:23px;margin-top:4px">Start your<br>free trial now</h2>
      <span class="dash"></span>
    </div>
    <p class="abs copy" style="left:85px;top:199px;width:322px">Lorem ipsum dolor sit amet, consetetur sadipscing elitr, sed diam nonumy eirmod tempor invidunt ut labore et dolore magna aliquyam erat, sed diam voluptua. At vero eos et accusam et justo duo dolores et ea rebum. Stet clita kasd</p>
    <span class="abs btn" style="left:85px;top:301px">Explore Our Platform</span>
    <div class="abs" style="left:865px;top:242px;width:46px;height:110px;background:var(--sky)"></div>
    <div class="abs" style="left:917px;top:223px;width:43px;height:136px;background:var(--violet)"></div>
    <div class="abs shot" style="left:434px;top:84px;width:440px;height:284px" role="img" aria-label="Laptop showing the platform's organization administration dashboard"></div>
  </section>

  <section class="context">
    <div class="abs" style="left:16px;top:245px;width:50px;height:103px;background:var(--violet)"></div>
    <div class="abs" style="left:69px;top:253px;width:48px;height:95px;background:var(--sky)"></div>
    <div class="abs" style="left:123px;top:316px;width:48px;height:32px;background:var(--violet)"></div>
    <div class="abs shot" style="left:79px;top:74px;width:422px;height:258px;border-radius:2px" role="img" aria-label="Platform dashboard screen with sidebar navigation and administration table"></div>
    <div class="abs" style="left:575px;top:111px">
      <div class="eyebrow">Unprecedented</div>
      <h2 class="display" style="font-size:23px;margin-top:4px">Context across<br>space and time</h2>
      <span class="dash"></span>
    </div>
    <p class="abs copy" style="left:575px;top:196px;width:325px">Lorem ipsum dolor sit amet, consetetur sadipscing elitr, sed diam nonumy eirmod tempor invidunt ut labore et dolore magna aliquyam erat, sed diam voluptua. At vero eos et accusam et justo duo dolores et ea rebum. Stet clita kasd</p>
    <span class="abs btn" style="left:575px;top:297px">Explore Our Platform</span>
  </section>

  <section class="services">
    <div class="abs services-photo" role="img" aria-label="Business professional holding a tablet surrounded by holographic data charts"></div>
    <div class="abs" style="left:526px;top:62px">
      <h2 class="display" style="font-size:22px;color:var(--white)">Our Services</h2>
      <span class="dash" style="background:var(--white);margin-left:62px"></span>
    </div>
    <p class="abs" style="left:526px;top:103px;width:330px;font-size:10.5px;line-height:14px;color:#dbe3f3">Lorem ipsum dolor sit amet, consetetur sadipscing elitr, sed diam nonumy eirmod tempor invidunt ut labore et dolore</p>
    <div class="abs service" style="top:161px">
      <span class="service-icon"><svg width="22" height="22" viewBox="0 0 22 22" fill="none" stroke="#dbe3f3" stroke-width="1.3"><circle cx="11" cy="11" r="4"/><path d="M11 2v4M11 16v4M2 11h4M16 11h4M5 5l3 3M14 14l3 3M17 5l-3 3M5 17l3-3"/></svg></span>
      <div><h3>Intelligent Observability</h3><p>Lorem ipsum dolor sit amet, consetetur sadipscing elitr, sed diam nonumy eirmod tempor invidunt ut</p></div>
    </div>
    <div class="abs service" style="top:231px">
      <span class="service-icon"><svg width="22" height="22" viewBox="0 0 22 22" fill="none" stroke="#dbe3f3" stroke-width="1.3"><circle cx="11" cy="11" r="2.5"/><circle cx="4" cy="5" r="1.8"/><circle cx="18" cy="5" r="1.8"/><circle cx="4" cy="17" r="1.8"/><circle cx="18" cy="17" r="1.8"/><path d="M5.5 6.3l3.6 3M16.5 6.3l-3.6 3M5.5 15.7l3.6-3M16.5 15.7l-3.6-3"/></svg></span>
      <div><h3>Continuous Automation</h3><p>Lorem ipsum dolor sit amet, consetetur sadipscing elitr, sed diam nonumy eirmod</p></div>
    </div>
    <div class="abs service" style="top:303px">
      <span class="service-icon"><svg width="22" height="22" viewBox="0 0 22 22" fill="none" stroke="#dbe3f3" stroke-width="1.3"><rect x="6" y="6" width="10" height="10" rx="1.5"/><path d="M9 2v4M13 2v4M9 16v4M13 16v4M2 9h4M2 13h4M16 9h4M16 13h4"/></svg></span>
      <div><h3>AI-Assistance</h3><p>Lorem ipsum dolor sit amet, consetetur sadipscing elitr, sed diam nonumy eirmod tempor invidunt ut labore et dolore magna aliquyam</p></div>
    </div>
  </section>

  <section class="about">
    <div class="abs" style="left:104px;top:134px">
      <div class="eyebrow">About Us</div>
      <h2 class="display" style="font-size:23px;margin-top:4px">Who we are</h2>
      <span class="dash"></span>
    </div>
    <p class="abs copy" style="left:104px;top:198px;width:350px;font-size:11px;line-height:17.5px">Lorem ipsum dolor sit amet, consetetur sadipscing elitr, sed diam nonumy eirmod tempor invidunt ut labore et dolore magna aliquyam erat, sed diam voluptua. At vero eos et accusam et justo duo dolores et ea rebum. Stet clita kasd gubergren, no sea takimata sanctus est Lorem ipsum dolor sit amet. Lorem ipsum dolor sit amet, consetetur sadipscing elitr, sed diam nonumy eirmod tempor invidunt ut labore et dolore</p>
    <span class="abs btn" style="left:104px;top:325px">Learn More</span>
    <svg class="abs" style="left:540px;top:52px" width="320" height="340" viewBox="0 0 320 340" role="img" aria-label="Three angled panels showing glowing financial charts">
      <defs><linearGradient id="panelFill" x1="0" y1="0" x2="1" y2="1"><stop offset="0" stop-color="#0b1f5c"/><stop offset=".5" stop-color="#1d5fb8"/><stop offset="1" stop-color="#081640"/></linearGradient></defs>
      <polygon points="0,105 75,100 75,290 0,283" fill="url(#panelFill)"/>
      <polygon points="88,74 178,64 178,307 88,297" fill="url(#panelFill)"/>
      <polygon points="194,30 312,0 312,337 194,312" fill="url(#panelFill)"/>
    </svg>
  </section>

  <section class="blog">
    <div class="abs" style="left:0;top:80px;width:960px;text-align:center">
      <h2 class="display" style="font-size:22px">Latest Blog</h2>
      <span class="dash" style="display:inline-block;margin-left:-14px;margin-top:12px"></span>
    </div>

    <div class="abs card-img" style="left:112px;background:linear-gradient(135deg,#0d2a66,#3170c4 55%,#0b1d4a)" role="img" aria-label="Hands working with a holographic analytics display"></div>
    <div class="abs card-body" style="left:137px">
      <h4>Lorem ipsum dolor sit amg hdy aeet, consetetur sadipscing elitr, sed</h4>
      <div class="card-date"><svg width="9" height="9" viewBox="0 0 9 9"><rect x=".5" y="1.5" width="8" height="7" fill="none" stroke="#2f6fe6"/><path d="M.5 3.5h8" stroke="#2f6fe6"/></svg>22 MAY 2021</div>
      <p>Lorem ipsum dolor sit amg hdy at, consetetur sadipscinger elitr, sed diam nonumy eirmod tenhmpor invidunt ut</p>
    </div>

    <div class="abs card-img" style="left:368px;background:linear-gradient(135deg,#2a2a2e,#6b5a4d 50%,#1e1e22)" role="img" aria-label="Analyst working at a computer in a dim office"></div>
    <div class="abs card-body" style="left:393px">
      <h4>Lorem ipsum dolor sit amg hdy aeet, consetetur sadipscing elitr, sed</h4>
      <div class="card-date"><svg width="9" height="9" viewBox="0 0 9 9"><rect x=".5" y="1.5" width="8" height="7" fill="none" stroke="#2f6fe6"/><path d="M.5 3.5h8" stroke="#2f6fe6"/></svg>22 MAY 2021</div>
      <p>Lorem ipsum dolor sit amg hdy at, consetetur sadipscinger elitr, sed diam nonumy eirmod tenhmpor invidunt ut</p>
    </div>

    <div class="abs card-img" style="left:624px;background:linear-gradient(135deg,#10223f,#3a6fb2 50%,#0e1a33)" role="img" aria-label="Operations room with multiple monitors displaying data"></div>
    <div class="abs card-body" style="left:649px">
      <h4>Lorem ipsum dolor sit amg hdy aeet, consetetur sadipscing elitr, sed</h4>
      <div class="card-date"><svg width="9" height="9" viewBox="0 0 9 9"><rect x=".5" y="1.5" width="8" height="7" fill="none" stroke="#2f6fe6"/><path d="M.5 3.5h8" stroke="#2f6fe6"/></svg>22 MAY 2021</div>
      <p>Lorem ipsum dolor sit amg hdy at, consetetur sadipscinger elitr, sed diam nonumy eirmod tenhmpor invidunt ut</p>
    </div>
  </section>

  <footer class="site-footer">
    <div class="abs brand" style="left:79px;top:84px;color:var(--white)"><span class="brand-mark"></span>Metrica Core</div>
    <p class="abs" style="left:79px;top:118px;width:240px;font-size:9.5px;line-height:12.5px">Lorem ipsum dolor sit amet, consetetur sadipscing elitr, sed diam nonumy eirmod tempor invidunt ut labore et dolore magna aliquyam erat,</p>

    <div class="abs f-head" style="left:380px">Usefull Links</div>
    <ul class="abs f-list" style="left:380px"><li>Home</li><li>About</li><li>Service</li><li>Blog</li><li>Platform</li></ul>

    <div class="abs f-head" style="left:557px">Contact Us</div>
    <div class="abs f-contact" style="left:557px">
      <div><svg width="8" height="11" viewBox="0 0 8 11"><path d="M4 0a4 4 0 0 0-4 4c0 3 4 7 4 7s4-4 4-7a4 4 0 0 0-4-4z" fill="#fff"/><circle cx="4" cy="4" r="1.4" fill="#0a1e3f"/></svg><span>48 Harrow Lane, Fenwick,<br>NY 10471</span></div>
      <div><svg width="9" height="9" viewBox="0 0 9 9"><path d="M1 .5l2 .2.8 2-1 .8a5 5 0 0 0 2.7 2.7l.8-1 2 .8.2 2-1 .8C4 8.6.4 5 .2 1.5z" fill="#fff"/></svg><span>+44(0)20 3000-1846</span></div>
      <div><svg width="9" height="8" viewBox="0 0 9 8"><rect x=".5" y=".5" width="8" height="7" fill="none" stroke="#fff"/><path d="M.5 .5l4 3.5 4-3.5" fill="none" stroke="#fff"/></svg><span>hello@metricacore.net</span></div>
    </div>

    <div class="abs f-head" style="left:750px">Social Links</div>
    <span class="abs social" style="left:771px;top:117px"></span>
    <span class="abs social" style="left:798px;top:117px"></span>
    <span class="abs social" style="left:825px;top:117px"></span>

    <div class="abs" style="left:137px;top:248px;width:685px;height:1px;background:#34476b"></div>
    <p class="abs" style="left:0;top:258px;width:960px;text-align:center;font-size:9px;color:#c9d3ea">© 2021 Norvane Holdings All Rights Reserved</p>
  </footer>

</div>
</body>
</html>
```